BrivaLOOM Web Design Project

We would like a website design to go with the new logo. They want something to model this site: http://www.harlenpoxby.com
Using the blue (#3366FF) and green (#33CC33). Like the bight colors in the top half of the home page. Must have a mini form on the interior pages.
Also like this site for inspiration:
http://www.daskelfinhaus.com/
Industry/Entity Type
Interior
Requirements
Must have
- Must fit the brief you had from before.
Must have a mini form
Should not have
- Doesn't have to have to pop up navigation over the slider on the home page.

```html
<!DOCTYPE html>
<html lang="en">
<head>
<meta charset="utf-8">
<title>BrivaLOOM</title>
<link href="https://fonts.googleapis.com/css2?family=Ubuntu:wght@400;500;700&display=swap" rel="stylesheet">
<style>
:root{
  --blue:#3366ff;
  --blue-soft:#5f86ee;
  --green:#33cc33;
  --green-dark:#2aa52a;
  --orange:#f26a21;
  --ink:#222;
  --text:#333;
  --grey-bg:#f1f1f1;
  --rule:#dddddd;
  --dark:#2b2b2b;
  --footer:#232323;
  --footer-link:#8a8a8a;
}
*{margin:0;padding:0;box-sizing:border-box}
html,body{width:1200px;height:1029px;overflow:hidden;background:#fff}
body{font-family:"Ubuntu",sans-serif;color:var(--text)}
.page{width:1400px;height:1200px;position:relative;transform:scale(.857142857);transform-origin:0 0}
.abs{position:absolute}

.topbar{left:0;top:0;width:1400px;height:34px;background:linear-gradient(#3a3a3a,#262626)}
.topbar__links{right:220px;top:10px;color:#fff;font-size:12px}

.brand{left:213px;top:92px;display:flex;align-items:center;gap:10px}
.brand__dot{width:22px;height:22px;border-radius:50%;background:var(--green)}
.brand__name{font-size:36px;font-weight:500;color:var(--blue);letter-spacing:-.5px}

.nav{left:615px;top:105px;width:785px;height:50px;background:linear-gradient(#4cd63f,#2db52a);display:flex;align-items:center}
.nav__item{font-size:16px;color:#173d12;margin-right:23px}
.nav__item--active{background:linear-gradient(#58e04a,#33c12f);color:#fff;height:50px;width:83px;display:flex;align-items:center;justify-content:center;margin-right:6px;font-weight:500}

.hero-rule{left:0;top:165px;width:1400px;height:7px;background:var(--blue)}
.hero{left:0;top:172px;width:1400px;height:433px;background:radial-gradient(ellipse at 40% 30%,#8aa6f5 0%,#6c8ef0 40%,#4c72e6 100%)}
.hero__visual{left:210px;top:265px;width:482px;height:265px;border-radius:6px;background:linear-gradient(135deg,#2d3b55,#1b2436)}
.hero__title{right:220px;top:190px;text-align:right;color:#fff;font-weight:700;line-height:1}
.hero__title span{display:block}
.hero__l1{font-size:58px}
.hero__l2{font-size:68px;margin-top:-2px}
.hero__l3{font-size:48px;margin-top:-4px}
.dots{left:214px;top:573px;width:124px;height:32px;background:#fff;border-radius:6px 6px 0 0;display:flex;align-items:center;justify-content:center;gap:7px}
.dots i{width:14px;height:14px;border-radius:50%;background:#cfcfcf}
.dots i.on{background:var(--blue)}

.intro{left:213px;top:630px;width:310px}
.intro__title{font-size:24px;font-weight:500;color:var(--blue);margin-bottom:4px}
.intro__text{font-size:12.5px;line-height:16px;color:var(--ink);padding-left:2px}
.more{color:var(--orange);font-size:13px;display:block;margin-top:6px}

.partners{left:623px;top:626px}
.section-title{font-size:20px;color:#333;font-weight:500}
.partner{background:#d9d9d9;border-radius:4px}

.divider{left:214px;top:771px;width:966px;height:1px;background:var(--rule)}
.services-title{left:215px;top:783px}
.arrow{top:822px;width:34px;height:155px;background:#f5f5f5;border-radius:6px;display:flex;align-items:center;justify-content:center}
.card{top:822px;width:204px;height:155px;background:var(--grey-bg);border-radius:6px;padding:14px 10px 0 22px}
.card__title{font-size:16px;font-weight:500;margin-bottom:6px}
.card__title--blue{color:var(--blue)}
.card__title--green{color:var(--green)}
.card__text{font-size:12.5px;line-height:16px;color:#333}
.card .more{margin-top:4px}

.footer{left:0;top:995px;width:1400px;height:205px;background:linear-gradient(#151515,var(--footer) 20px)}
.fcol{top:1012px}
.fcol h4{color:#fff;font-size:15px;font-weight:700;margin-bottom:14px}
.fcol a{display:block;color:var(--footer-link);font-size:11px;line-height:24px;text-decoration:none}
.news{left:980px;top:1008px;width:195px;height:22px;display:flex}
.news__input{flex:1;background:#fff;border-radius:3px 0 0 3px;font-size:12px;color:#777;padding:3px 6px}
.news__go{width:30px;background:var(--blue);color:#fff;font-size:12px;font-weight:700;text-align:center;line-height:22px;border-radius:0 3px 3px 0}
.social{width:92px;height:30px;background:linear-gradient(#2f2f2f,#1c1c1c);border:1px solid #444;border-radius:3px;display:flex;align-items:center;gap:9px;color:#fff;font-size:11px;padding-left:3px}
.social__sq{width:22px;height:22px;border-radius:2px}
</style>
</head>
<body>
<div class="page">
  <div class="abs topbar"><span class="abs topbar__links">Member login &nbsp;|&nbsp; Register</span></div>

  <div class="abs brand"><span class="brand__dot"></span><span class="brand__name">BrivaLOOM</span></div>

  <nav class="abs nav">
    <span class="nav__item nav__item--active">Home</span>
    <span class="nav__item">Products &amp; Services</span>
    <span class="nav__item">Partners</span>
    <span class="nav__item">Careers</span>
    <span class="nav__item">About us</span>
    <span class="nav__item">Contact us</span>
  </nav>

  <div class="abs hero-rule"></div>
  <section class="abs hero"></section>
  <div class="abs hero__visual" role="img" aria-label="Tablet and three smartphones showing a home screen"></div>
  <h1 class="abs hero__title"><span class="hero__l1">Lorem Ipsum is</span><span class="hero__l2">simply dummy</span><span class="hero__l3">text of the printing</span></h1>
  <div class="abs dots"><i></i><i></i><i></i><i class="on"></i><i></i></div>

  <section class="abs intro">
    <h2 class="intro__title">BrivaLOOM</h2>
    <p class="intro__text">BrivaLOOM is a one stop solution for all business technology needs. The Team’s vast experience and in-depth domain knowledge certainly adds value to its customers.</p>
    <span class="more">read more</span>
  </section>

  <h3 class="abs partners section-title">Our Partners</h3>
  <div class="abs partner" style="left:625px;top:662px;width:90px;height:42px"></div>
  <div class="abs partner" style="left:745px;top:662px;width:85px;height:40px"></div>
  <div class="abs partner" style="left:862px;top:655px;width:62px;height:50px"></div>
  <div class="abs partner" style="left:962px;top:664px;width:88px;height:26px"></div>
  <div class="abs partner" style="left:1070px;top:664px;width:98px;height:32px"></div>
  <div class="abs partner" style="left:628px;top:722px;width:70px;height:30px"></div>

  <div class="abs divider"></div>
  <h3 class="abs services-title section-title">Top Services</h3>

  <div class="abs arrow" style="left:214px"><svg width="20" height="40" viewBox="0 0 20 40"><path d="M16 3 4 20l12 17" fill="none" stroke="#d8d8d8" stroke-width="4"/></svg></div>
  <div class="abs arrow" style="left:1146px"><svg width="20" height="40" viewBox="0 0 20 40"><path d="M4 3l12 17L4 37" fill="none" stroke="#d8d8d8" stroke-width="4"/></svg></div>

  <article class="abs card" style="left:263px"><h4 class="card__title card__title--blue">Technical Support</h4><p class="card__text">Lorem ipsum dolor sit amet, consectetuer adipiscing elit sed diam nonummy nibh euismod tincidunt ut laoreet dolore magna.</p><span class="more">read more</span></article>
  <article class="abs card" style="left:484px"><h4 class="card__title card__title--green">Network Solutions</h4><p class="card__text">Lorem ipsum dolor sit amet, consectetuer adipiscing elit sed diam nonummy nibh euismod tincidunt ut laoreet dolore magna.</p><span class="more">read more</span></article>
  <article class="abs card" style="left:705px"><h4 class="card__title card__title--blue">Database Management</h4><p class="card__text">Lorem ipsum dolor sit amet, consectetuer adipiscing elit sed diam nonummy nibh euismod tincidunt ut laoreet dolore magna.</p><span class="more">read more</span></article>
  <article class="abs card" style="left:926px"><h4 class="card__title card__title--green">Web Development</h4><p class="card__text">Lorem ipsum dolor sit amet, consectetuer adipiscing elit sed diam nonummy nibh euismod tincidunt ut laoreet dolore magna.</p><span class="more">read more</span></article>

  <footer class="abs footer"></footer>
  <div class="abs fcol" style="left:226px;top:1014px"><h4>INFORMATION</h4><a>Contact</a><a>Delivery</a><a>Legal Notice</a><a>Terms and Conditions</a><a>About Us</a></div>
  <div class="abs fcol" style="left:422px"><h4>Downloads</h4><a>Contact</a><a>Delivery</a><a>Legal Notice</a><a>Terms and Conditions</a><a>About Us</a></div>
  <div class="abs fcol" style="left:618px"><h4>Downloads</h4><a>Contact</a><a>Delivery</a><a>Legal Notice</a><a>Terms and Conditions</a><a>About Us</a></div>
  <div class="abs fcol" style="left:814px;top:1007px"><h4>About Us</h4><a>Contact</a><a>Delivery</a><a>Legal Notice</a><a>Terms and Conditions</a><a>About Us</a></div>

  <form class="abs news"><span class="news__input">Subscribe Newsletter</span><span class="news__go">Go</span></form>
  <div class="abs social" style="left:980px;top:1040px"><span class="social__sq" style="background:#1b6ea8"></span>Linkora</div>
  <div class="abs social" style="left:1082px;top:1040px"><span class="social__sq" style="background:#c8312a"></span>Gloopa +</div>
  <div class="abs social" style="left:980px;top:1078px"><span class="social__sq" style="background:#36589a"></span>Facelane</div>
  <div class="abs social" style="left:1082px;top:1078px"><span class="social__sq" style="background:#b3212a"></span>Pinvault</div>
  <div class="abs social" style="left:980px;top:1116px"><span class="social__sq" style="background:#3a9fd8"></span>Chirply</div>
  <div class="abs social" style="left:1082px;top:1116px"><span class="social__sq" style="background:#f07a1a"></span>RSS feed</div>
</div>
</body>
</html>
```